SubHarbor Flyer - Substitute Management Software

I need a flyer to send to schools talking about our new product SubHarbor. I have added a file with wording. Please ignore the formatting and design a brochure that I can be proud of. I also want to add the product logo (SubHarbor) as well as the company logo (Brightline Planning Group). I have added a screenshot of the product if helpful. It can be used in brochure or not. If you need anything from me please don't be shy and ask.

Target Market(s)

Schools

```html
<!DOCTYPE html>
<html lang="en">
<head>
<meta charset="utf-8">
<title>SubHarbor – Core Capabilities</title>
<link href="https://fonts.googleapis.com/css2?family=Montserrat:wght@300;700;800&family=Manrope:wght@600;700&display=swap" rel="stylesheet">
<style>
  :root{
    --bg-top:#5a4f9c;
    --bg-mid:#6b8ac4;
    --bg-bottom:#6a5ba9;
    --text:#ffffff;
    --logo-red:#8c2a2e;
    --pill-border:#5a4f9c;
    --art-sky:#cfe6f5;
    --art-blue:#7aa7dc;
    --art-green:#6cbf5a;
    --art-coral:#ee6f6f;
  }
  *{margin:0;padding:0;box-sizing:border-box}
  html,body{width:927px;height:1200px;overflow:hidden}
  body{
    position:relative;
    color:var(--text);
    font-family:"Manrope",sans-serif;
    background:linear-gradient(180deg,var(--bg-top) 0%,var(--bg-mid) 48%,#6f86c2 68%,var(--bg-bottom) 100%);
  }
  .abs{position:absolute}
  .page-title{left:26px;top:20px;font:800 34px/1 "Montserrat",sans-serif;letter-spacing:-.3px}
  .section-title{left:26px;font:300 31px/36px "Montserrat",sans-serif;letter-spacing:-.2px}
  .sub-title{left:26px;font:700 19px/1 "Montserrat",sans-serif}
  .bullets{left:26px;list-style:none;font-weight:700;font-size:12.2px;line-height:14px}
  .bullets li{position:relative;padding-left:17px}
  .bullets li::before{content:"";position:absolute;left:1px;top:3px;width:8px;height:8px;border-radius:50%;background:var(--text)}
  .bullets .lead{font-size:15px;line-height:16px}
  .bullets .lead::before{top:4px}
  .detail{left:43px;font-weight:700;font-size:12.2px;line-height:12px}
  .art{border-radius:46% 54% 40% 48%/52% 44% 56% 48%}
  .art-absence{left:629px;top:66px;width:241px;height:247px;background:linear-gradient(160deg,var(--art-sky),#eef6fb 60%,#f3a64a 100%)}
  .art-placement{left:609px;top:414px;width:256px;height:204px;background:linear-gradient(170deg,var(--art-blue),var(--art-sky) 55%,#e6f1f8)}
  .art-team{left:598px;top:736px;width:278px;height:184px;background:linear-gradient(180deg,#d9e8f5,var(--art-coral) 50%,var(--art-green) 80%)}
  .brand-pill{left:357px;top:1048px;width:214px;height:79px;border-radius:40px;background:#fff;border:3px solid var(--pill-border);outline:2px solid #fff;display:flex;align-items:center;justify-content:center;gap:8px}
  .brand-pill .dot{width:12px;height:12px;border-radius:50%;background:var(--logo-red);flex:none}
  .brand-pill .name{color:var(--logo-red);font:700 14px/16px "Manrope",sans-serif;width:130px}
  .contact{top:1139px;left:0;width:927px;display:flex;justify-content:center;align-items:center;gap:14px;font:700 14px/1 "Manrope",sans-serif;white-space:nowrap}
  .contact .item{display:flex;align-items:center;gap:10px}
  .contact svg{width:22px;height:22px;flex:none}
</style>
</head>
<body>
  <h1 class="abs page-title">Core Capabilities</h1>

  <h2 class="abs section-title" style="top:70px">Smart Absence &amp; Leave<br>Management</h2>
  <ul class="abs bullets" style="top:154px">
    <li style="margin-bottom:10px">Centralized dashboard to track absences across the district</li>
    <li style="margin-bottom:10px">Digital approval workflows (configure which absence<br>reasons require approval)</li>
    <li style="margin-bottom:11px">Daily absence limits and visibility into staffing levels</li>
    <li style="margin-bottom:11px">Leave balance management and absence history tracking</li>
    <li>Fine-grained permissions to control access by role</li>
  </ul>
  <div class="abs art art-absence" role="img" aria-label="Illustration of a woman tapping a calendar on a large phone screen"></div>

  <h2 class="abs section-title" style="top:277px">Automated Substitute Placement &amp;<br>Scheduling Flexibility</h2>
  <h3 class="abs sub-title" style="top:361px">Automatically matches and fills jobs based on:</h3>
  <ul class="abs bullets" style="top:392px">
    <li style="margin-bottom:10.5px">Availability and voting algorithms</li>
    <li style="margin-bottom:10.5px">Qualifications / certifications / Category</li>
    <li style="margin-bottom:10.5px">School, grade, teacher preferences and exclusion lists</li>
    <li>School and role requirements</li>
  </ul>

  <h3 class="abs sub-title" style="top:495px">Supports complex district needs:</h3>
  <ul class="abs bullets" style="top:528px">
    <li style="margin-bottom:10.5px">Multiple positions per employee (one person, multiple roles/schedules)</li>
    <li style="margin-bottom:10.5px">Partial fill capability (fill part of a day, split coverage, or swap assignments)</li>
    <li style="margin-bottom:10.5px">Schedule multiple substitutes at once</li>
    <li style="margin-bottom:10.5px">Quick reassignment tools when plans change</li>
    <li>Prearranged subs and priority substitute notifications</li>
  </ul>
  <div class="abs art art-placement" role="img" aria-label="Illustration of two colleagues working at a desk with a scheduling chart"></div>

  <h3 class="abs sub-title" style="top:656px">Designed for Administrative Efficiency</h3>
  <ul class="abs bullets" style="top:688px"><li class="lead">Actionable reporting:</li></ul>
  <p class="abs detail" style="top:717px">See daily absence and fill status at a glance, with built-in and custom<br>reports to analyze trends and improve coverage.</p>
  <ul class="abs bullets" style="top:750px"><li class="lead">Time-saving integrations:</li></ul>
  <p class="abs detail" style="top:778px">Connect SubHarbor with your payroll systems to streamline exports,<br>reduce duplicate entry, and minimize payroll errors</p>

  <h3 class="abs sub-title" style="top:818px">Substitute-friendly tools:</h3>
  <ul class="abs bullets" style="top:851px;line-height:15px">
    <li style="margin-bottom:15px">A free mobile app lets subs set availability, manage and accept jobs on the<br>go, and access job details plus school profiles that help them feel<br>welcomed and prepared before they arrive.</li>
    <li>Substitutes can choose how they want to be contacted and accept jobs<br>quickly.</li>
  </ul>
  <div class="abs art art-team" role="img" aria-label="Illustration of a team working together around charts and a large ball"></div>

  <h3 class="abs sub-title" style="top:963px">Ready to increase fill rates and reduce absence chaos?</h3>
  <ul class="abs bullets" style="top:995px;line-height:15px">
    <li>Schedule a quick SubHarbor demo and see how districts streamline approvals,<br>outreach, and coverage in one system.</li>
  </ul>

  <div class="abs brand-pill"><span class="dot"></span><span class="name">Brightline Planning Group</span></div>

  <div class="abs contact">
    <div class="item">
      <svg viewBox="0 0 24 24" fill="none" stroke="#fff" stroke-width="1.3"><circle cx="12" cy="12" r="11"/><path d="M8.5 6.5l2 2-1.2 1.6a7 7 0 0 0 4.6 4.6l1.6-1.2 2 2-1.5 1.6c-4.5 0-9.5-5-9.5-9.5z"/></svg>
      <span>555-310-4827</span>
    </div>
    <div class="item">
      <svg viewBox="0 0 24 24" fill="none" stroke="#fff" stroke-width="1.3"><circle cx="12" cy="12" r="11"/><rect x="6.5" y="8" width="11" height="8" rx="1"/><path d="M6.5 8.5l5.5 4 5.5-4"/></svg>
      <span>sales@brightlineplanning.com</span>
    </div>
    <div class="item">
      <svg viewBox="0 0 24 24" fill="none" stroke="#fff" stroke-width="1.3"><circle cx="12" cy="12" r="10"/><ellipse cx="12" cy="12" rx="4.5" ry="10"/><path d="M2 12h20M4 7h16M4 17h16"/></svg>
      <span>www.brightlineplanning.com</span>
    </div>
  </div>
</body>
</html>
```